Web Dashboard for manufacturing data

We need a dashboard for website to show statistical information on buttons/cards/tiles. There will be 12 buttons on the screen (laptop, tablet) On these buttons there are several key pieces of information on each button. 1) Largest info is % 0-100%. 2) 4 status colours neutral, green, yellow, red. 3) Title- up to 20 characters 4) target here is an example... target=above 90%.- When these buttons are tapped, they take user to more info for that specific data.
1 page

```html
<!DOCTYPE html>
<html lang="en">
<head>
<meta charset="UTF-8">
<title>Orvadine – Manufacturing Dashboard</title>
<link rel="stylesheet" href="https://fonts.googleapis.com/css2?family=Poppins:wght@400;500;600;700&display=swap">
<style>
  :root {
    --brand-blue: #0457b0;
    --card-blue: #0459b3;
    --content-bg: #cddff0;
    --white: #ffffff;
    --nav-text: #b9d2f0;
    --dial-face: #7fa8d4;
    --dial-text: #24476e;
    --track: #2d6fbd;
    --status-green: #3fe04a;
    --status-yellow: #f2d21b;
    --status-red: #e0252e;
    --status-neutral: #9fb3c8;
  }
  * { box-sizing: border-box; margin: 0; padding: 0; }
  html, body { width: 1200px; height: 829px; overflow: hidden; }
  body {
    font-family: "Poppins", sans-serif;
    display: flex;
    background: var(--content-bg);
  }
  .sidebar {
    width: 290px;
    height: 100%;
    background: var(--brand-blue);
    padding-top: 48px;
    flex-shrink: 0;
  }
  .brand {
    display: flex;
    align-items: center;
    gap: 14px;
    padding-left: 38px;
    margin-bottom: 50px;
  }
  .brand-mark {
    width: 34px; height: 34px;
    border-radius: 8px;
    background: var(--white);
  }
  .brand-name {
    color: var(--white);
    font-weight: 600;
    font-size: 26px;
    letter-spacing: 0.2px;
  }
  .nav { list-style: none; }
  .nav-item {
    display: flex;
    align-items: center;
    gap: 22px;
    height: 56px;
    margin-left: 38px;
    padding-left: 22px;
    margin-bottom: 16px;
    color: var(--nav-text);
    font-size: 16px;
    font-weight: 500;
  }
  .nav-item svg { width: 30px; height: 30px; flex-shrink: 0; }
  .nav-item--active {
    background: var(--white);
    color: var(--brand-blue);
    border-radius: 28px 0 0 28px;
    font-weight: 600;
  }
  .content {
    flex: 1;
    padding: 100px 0 0 70px;
  }
  .tile-grid {
    display: grid;
    grid-template-columns: repeat(4, 145px);
    grid-auto-rows: 196px;
    column-gap: 66px;
    row-gap: 48px;
  }
  .stat-tile {
    background: var(--card-blue);
    border-radius: 3px;
    box-shadow: 6px 8px 12px rgba(20, 50, 90, 0.45);
    display: flex;
    flex-direction: column;
    align-items: center;
    padding-top: 10px;
    color: var(--white);
    text-align: center;
    text-decoration: none;
  }
  .dial { position: relative; width: 86px; height: 86px; }
  .dial svg { position: absolute; inset: 0; width: 100%; height: 100%; }
  .dial-value {
    position: absolute;
    inset: 0;
    display: flex;
    align-items: center;
    justify-content: center;
    color: var(--dial-text);
    font-size: 15px;
    font-weight: 600;
  }
  .tile-title {
    margin-top: 16px;
    font-size: 13.5px;
    font-weight: 600;
    line-height: 1.25;
  }
  .tile-target {
    margin-top: 10px;
    font-size: 8px;
    font-weight: 600;
    line-height: 1.5;
  }
  .track { fill: none; stroke: var(--track); stroke-width: 5; stroke-linecap: round; stroke-dasharray: 142.4 213.6; }
  .arc { fill: none; stroke-width: 5; stroke-linecap: round; }
  .arc--green { stroke: var(--status-green); }
  .arc--yellow { stroke: var(--status-yellow); }
  .arc--red { stroke: var(--status-red); }
  .face { fill: var(--dial-face); }
</style>
</head>
<body>
  <aside class="sidebar">
    <div class="brand">
      <span class="brand-mark"></span>
      <span class="brand-name">Orvadine</span>
    </div>
    <ul class="nav">
      <li class="nav-item nav-item--active">
        <svg viewBox="0 0 30 30" fill="none" stroke="currentColor" stroke-width="2" stroke-linejoin="round"><path d="M5 13 L15 5 L25 13 V25 H5 Z"/><path d="M12 25 V18 H18 V25"/></svg>
        Dashboard
      </li>
      <li class="nav-item">
        <svg viewBox="0 0 30 30" fill="none" stroke="currentColor" stroke-width="1.8"><rect x="5" y="7" width="20" height="18" rx="2"/><path d="M5 12 H25 M10 4 V9 M20 4 V9"/></svg>
        Event
      </li>
      <li class="nav-item">
        <svg viewBox="0 0 30 30" fill="none" stroke="currentColor" stroke-width="1.8" stroke-linejoin="round"><circle cx="18" cy="9" r="5"/><path d="M4 20 L9 18 H16 a2 2 0 0 1 0 4 H11 M16 22 L24 18 a2 2 0 0 1 2 3 L16 27 H6"/></svg>
        Finance
      </li>
      <li class="nav-item">
        <svg viewBox="0 0 30 30" fill="none" stroke="currentColor" stroke-width="1.8"><circle cx="15" cy="10" r="5"/><path d="M6 26 V23 a6 6 0 0 1 6 -6 H18 a6 6 0 0 1 6 6 V26 Z"/></svg>
        User
      </li>
      <li class="nav-item">
        <svg viewBox="0 0 30 30" fill="none" stroke="currentColor" stroke-width="1.8" stroke-linejoin="round"><path d="M10 6 H26 V17 H22 L19 20 V17 H10 Z"/><path d="M7 11 H4 V22 H7 V26 L11 22 H18"/></svg>
        Chat
      </li>
      <li class="nav-item">
        <svg viewBox="0 0 30 30" fill="none" stroke="currentColor" stroke-width="2" stroke-linejoin="round" stroke-linecap="round"><path d="M3 16 H9 L12 7 L17 24 L20 14 H27"/></svg>
        Lastest Activity
      </li>
    </ul>
  </aside>

  <main class="content">
    <div class="tile-grid">
      <a class="stat-tile"><div class="dial"><svg viewBox="0 0 80 80"><circle class="face" cx="40" cy="40" r="29"/><circle class="track" cx="40" cy="40" r="34" transform="rotate(150 40 40)"/><circle class="arc arc--green" cx="40" cy="40" r="34" stroke-dasharray="129.6 213.6" transform="rotate(150 40 40)"/></svg><span class="dial-value">91%</span></div><p class="tile-title">Example<br>TitleUpTo 20</p><p class="tile-target">Target:<br>above 90%</p></a>
      <a class="stat-tile"><div class="dial"><svg viewBox="0 0 80 80"><circle class="face" cx="40" cy="40" r="29"/><circle class="track" cx="40" cy="40" r="34" transform="rotate(150 40 40)"/><circle class="arc arc--yellow" cx="40" cy="40" r="34" stroke-dasharray="121 213.6" transform="rotate(150 40 40)"/></svg><span class="dial-value">85%</span></div><p class="tile-title">Example<br>TitleUpTo 20</p><p class="tile-target">Target:<br>above 90%</p></a>
      <a class="stat-tile"><div class="dial"><svg viewBox="0 0 80 80"><circle class="face" cx="40" cy="40" r="29"/><circle class="track" cx="40" cy="40" r="34" transform="rotate(150 40 40)"/><circle class="arc arc--red" cx="40" cy="40" r="34" stroke-dasharray="72.6 213.6" transform="rotate(150 40 40)"/></svg><span class="dial-value">51%</span></div><p class="tile-title">Example<br>TitleUpTo 20</p><p class="tile-target">Target:<br>above 90%</p></a>
      <a class="stat-tile"><div class="dial"><svg viewBox="0 0 80 80"><circle class="face" cx="40" cy="40" r="29"/><circle class="track" cx="40" cy="40" r="34" transform="rotate(150 40 40)"/><circle class="arc arc--green" cx="40" cy="40" r="34" stroke-dasharray="129.6 213.6" transform="rotate(150 40 40)"/></svg><span class="dial-value">91%</span></div><p class="tile-title">Example<br>TitleUpTo 20</p><p class="tile-target">Target:<br>above 90%</p></a>

      <a class="stat-tile"><div class="dial"><svg viewBox="0 0 80 80"><circle class="face" cx="40" cy="40" r="29"/><circle class="track" cx="40" cy="40" r="34" transform="rotate(150 40 40)"/><circle class="arc arc--green" cx="40" cy="40" r="34" stroke-dasharray="129.6 213.6" transform="rotate(150 40 40)"/></svg><span class="dial-value">91%</span></div><p class="tile-title">Example<br>TitleUpTo 20</p><p class="tile-target">Target:<br>above 90%</p></a>
      <a class="stat-tile"><div class="dial"><svg viewBox="0 0 80 80"><circle class="face" cx="40" cy="40" r="29"/><circle class="track" cx="40" cy="40" r="34" transform="rotate(150 40 40)"/><circle class="arc arc--green" cx="40" cy="40" r="34" stroke-dasharray="129.6 213.6" transform="rotate(150 40 40)"/></svg><span class="dial-value">91%</span></div><p class="tile-title">Example<br>TitleUpTo 20</p><p class="tile-target">Target:<br>above 90%</p></a>
      <a class="stat-tile"><div class="dial"><svg viewBox="0 0 80 80"><circle class="face" cx="40" cy="40" r="29"/><circle class="track" cx="40" cy="40" r="34" transform="rotate(150 40 40)"/><circle class="arc arc--green" cx="40" cy="40" r="34" stroke-dasharray="129.6 213.6" transform="rotate(150 40 40)"/></svg><span class="dial-value">91%</span></div><p class="tile-title">Example<br>TitleUpTo 20</p><p class="tile-target">Target:<br>above 90%</p></a>
      <a class="stat-tile"><div class="dial"><svg viewBox="0 0 80 80"><circle class="face" cx="40" cy="40" r="29"/><circle class="track" cx="40" cy="40" r="34" transform="rotate(150 40 40)"/><circle class="arc arc--green" cx="40" cy="40" r="34" stroke-dasharray="129.6 213.6" transform="rotate(150 40 40)"/></svg><span class="dial-value">91%</span></div><p class="tile-title">Example<br>TitleUpTo 20</p><p class="tile-target">Target:<br>above 90%</p></a>

      <a class="stat-tile"><div class="dial"><svg viewBox="0 0 80 80"><circle class="face" cx="40" cy="40" r="29"/><circle class="track" cx="40" cy="40" r="34" transform="rotate(150 40 40)"/><circle class="arc arc--green" cx="40" cy="40" r="34" stroke-dasharray="129.6 213.6" transform="rotate(150 40 40)"/></svg><span class="dial-value">91%</span></div><p class="tile-title">Example<br>TitleUpTo 20</p><p class="tile-target">Target:<br>above 90%</p></a>
      <a class="stat-tile"><div class="dial"><svg viewBox="0 0 80 80"><circle class="face" cx="40" cy="40" r="29"/><circle class="track" cx="40" cy="40" r="34" transform="rotate(150 40 40)"/><circle class="arc arc--green" cx="40" cy="40" r="34" stroke-dasharray="129.6 213.6" transform="rotate(150 40 40)"/></svg><span class="dial-value">91%</span></div><p class="tile-title">Example<br>TitleUpTo 20</p><p class="tile-target">Target:<br>above 90%</p></a>
      <a class="stat-tile"><div class="dial"><svg viewBox="0 0 80 80"><circle class="face" cx="40" cy="40" r="29"/><circle class="track" cx="40" cy="40" r="34" transform="rotate(150 40 40)"/><circle class="arc arc--green" cx="40" cy="40" r="34" stroke-dasharray="129.6 213.6" transform="rotate(150 40 40)"/></svg><span class="dial-value">91%</span></div><p class="tile-title">Example<br>TitleUpTo 20</p><p class="tile-target">Target:<br>above 90%</p></a>
      <a class="stat-tile"><div class="dial"><svg viewBox="0 0 80 80"><circle class="face" cx="40" cy="40" r="29"/><circle class="track" cx="40" cy="40" r="34" transform="rotate(150 40 40)"/><circle class="arc arc--green" cx="40" cy="40" r="34" stroke-dasharray="129.6 213.6" transform="rotate(150 40 40)"/></svg><span class="dial-value">91%</span></div><p class="tile-title">Example<br>TitleUpTo 20</p><p class="tile-target">Target:<br>above 90%</p></a>
    </div>
  </main>
</body>
</html>
```